Billboard

we want our Hop & Skip logo really big, we need this to stand out

Use a really bold font for the wording as it's on a billboard on the highway

Hop & Skip Logo
perhaps on left hand side really large then have a slanting line and a different colour background for the other side.

Wording BELOW-bold

TOUR NOW

hopandskip.edu.au

Use one image,
I have attached other designs we have been using for our campaign so a similar look would be great.
specs- 1224 W × 324 H px JPEG

Target Market(s)
families

Industry/Entity Type
childcare

Target Market(s)

families

Industry/Entity Type

childcare

Requirements
Must have
• bold font and big logo

```html
<!DOCTYPE html>
<html lang="en">
<head>
<meta charset="utf-8">
<title>Hop &amp; Skip Billboard</title>
<link href="https://fonts.googleapis.com/css2?family=Anton&display=swap" rel="stylesheet">
<style>
  :root {
    --sky-blue: #03aeef;
    --sun-yellow: #f7ec00;
    --band-red: #e8352e;
    --ink: #111111;
    --white: #ffffff;
    --backdrop: #d9d9d9;
  }
  html, body {
    margin: 0;
    padding: 0;
    width: 996px;
    height: 1200px;
    overflow: hidden;
    background: var(--backdrop);
  }
  .billboard {
    position: absolute;
    left: 28px;
    top: 476px;
    width: 940px;
    height: 248px;
    overflow: hidden;
    background: var(--sun-yellow);
    box-shadow: 0 4px 10px rgba(0,0,0,0.25);
    font-family: "Anton", "Impact", sans-serif;
  }
  .brand-panel {
    position: absolute;
    left: 0;
    top: 0;
    width: 420px;
    height: 100%;
    background: var(--sky-blue);
  }
  .brand-lockup {
    position: absolute;
    left: 0;
    top: 0;
    width: 230px;
    height: 100%;
    display: flex;
    flex-direction: column;
    align-items: center;
    justify-content: center;
    gap: 14px;
  }
  .brand-dot {
    width: 64px;
    height: 64px;
    border-radius: 50%;
    background: var(--sun-yellow);
  }
  .brand-name {
    color: var(--white);
    font-size: 46px;
    line-height: 1;
    letter-spacing: 0.5px;
    white-space: nowrap;
  }
  .photo-frame {
    position: absolute;
    left: 236px;
    top: -14px;
    width: 356px;
    height: 272px;
    border-radius: 50%;
    border: 5px solid var(--white);
    box-sizing: border-box;
    background: radial-gradient(ellipse at 50% 40%, #d9a878 0%, #b98a5e 45%, #5d6b3a 100%);
  }
  .headline {
    position: absolute;
    left: 620px;
    top: 72px;
    width: 300px;
    margin: 0;
    text-align: center;
    color: var(--white);
    font-size: 68px;
    font-weight: 400;
    line-height: 1;
    letter-spacing: 0.5px;
    -webkit-text-stroke: 2px var(--ink);
    text-shadow: 4px 4px 0 var(--ink);
  }
  .web-band {
    position: absolute;
    left: 582px;
    top: 158px;
    width: 358px;
    height: 45px;
    background: var(--band-red);
    clip-path: polygon(4% 0, 100% 0, 100% 100%, 0 100%);
    display: flex;
    align-items: center;
    justify-content: center;
  }
  .web-address {
    color: var(--white);
    font-size: 32px;
    line-height: 1;
    padding-left: 18px;
  }
</style>
</head>
<body>
  <section class="billboard">
    <div class="brand-panel"></div>
    <div class="brand-lockup">
      <div class="brand-dot"></div>
      <div class="brand-name">Hop &amp; Skip</div>
    </div>
    <div class="photo-frame" role="img" aria-label="Photo of young children in sun hats playing with buckets and spades in a sandpit"></div>
    <h1 class="headline">TOUR NOW</h1>
    <div class="web-band">
      <span class="web-address">hopandskip.edu.au</span>
    </div>
  </section>
</body>
</html>
```